Brisk Fixworks business card

I need business card for my business, I think you have all my details.six months ago I design with you car wrap design. We would like to design both side of the card. On front of card we would like logo , Name and our contact details.
At the back we are looking to mentioned our services.
The name will be:
Gulbadin Norzai
Managing Director
Ph:07955384217
Email:info@brisk-fixworks.com
Web:www.brisk-fixworks.com
So we have our logo, you don’t need to change the logo.
Please see the attachment.
Thanks

Target Market(s)

Home improvement

Industry/Entity Type

Home Improvement

Contact Information for Business Card

Company name: Brisk Fixworks
Name: Gulbadin Norzai
Position: Director
Ph:07955384217
Web: www.brisk-fixworks.com
Add: 14 Garwick Lane
Ashcombe
TW3 9QL
SECOND PERSON
Nasrullah norzai
Position: Handyman
Ph: 07822 643157
Email: info@brisk-fixworks.com
Add: 62 Bramcote Vale Drive
Ashcombe
TW7 2KD

```html
<!DOCTYPE html>
<html lang="en">
<head>
<meta charset="utf-8">
<title>Brisk Fixworks – Business Card</title>
<link rel="stylesheet" href="https://fonts.googleapis.com/css2?family=Montserrat:wght@400;500;600;700;800&display=swap">
<style>
  :root {
    --brand-red: #e31b2b;
    --brand-blue: #27378c;
    --ink: #1c1c1c;
    --paper: #ffffff;
    --stage: #2b2b2b;
  }
  * { box-sizing: border-box; margin: 0; padding: 0; }
  html, body {
    width: 1200px; height: 780px; overflow: hidden;
    background: var(--stage);
    font-family: "Montserrat", Arial, sans-serif;
  }
  .card {
    position: absolute; width: 640px; height: 360px;
    background: var(--brand-red);
    overflow: hidden;
    box-shadow: 0 14px 30px rgba(0,0,0,.45);
  }
  .card--back { left: 60px; top: 24px; }
  .card--front { left: 500px; top: 396px; }
  .card__shape { position: absolute; inset: 0; width: 100%; height: 100%; }

  .brand {
    position: absolute; display: flex; align-items: center; gap: 8px;
    color: var(--brand-blue); font-weight: 800; letter-spacing: .5px;
    white-space: nowrap;
  }
  .brand__mark { width: 14px; height: 14px; background: var(--brand-red); flex: none; }
  .card--back .brand { left: 222px; top: 32px; font-size: 22px; }
  .card--front .brand { left: 56px; top: 62px; font-size: 28px; }
  .card--front .brand__mark { width: 18px; height: 18px; }

  .services-tag {
    position: absolute; left: 214px; top: 72px; width: 212px; height: 22px;
    background: var(--brand-red); border-radius: 11px;
    color: var(--paper); font-weight: 700; font-size: 13px; letter-spacing: .5px;
    display: flex; align-items: center; justify-content: center;
  }
  .services {
    position: absolute; left: 236px; top: 100px; list-style: none;
    color: var(--ink); font-weight: 800; line-height: .98; letter-spacing: .3px;
    white-space: nowrap;
  }
  .services li:nth-child(1), .services li:nth-child(2), .services li:nth-child(8) { font-size: 20px; }
  .services li:nth-child(3), .services li:nth-child(7) { font-size: 23px; }
  .services li:nth-child(4) { font-size: 25px; }
  .services li:nth-child(5) { font-size: 27px; }
  .services li:nth-child(6) { font-size: 29px; }

  .person { position: absolute; left: 60px; top: 162px; }
  .person__name { color: var(--brand-blue); font-weight: 700; font-size: 27px; letter-spacing: 1px; text-transform: uppercase; white-space: nowrap; }
  .person__role { color: var(--ink); font-weight: 500; font-size: 14px; letter-spacing: 4px; margin-top: 2px; }

  .contacts { position: absolute; left: 60px; top: 232px; list-style: none; }
  .contacts li {
    display: flex; align-items: center; gap: 10px; height: 26px;
    color: var(--ink); font-size: 15px; font-weight: 500; white-space: nowrap;
  }
  .contacts__icon {
    width: 20px; height: 20px; border-radius: 4px; background: var(--brand-red);
    display: flex; align-items: center; justify-content: center; flex: none;
  }
  .contacts__icon svg { width: 13px; height: 13px; }
</style>
</head>
<body>

<section class="card card--back" aria-label="Card back: services">
  <svg class="card__shape" viewBox="0 0 640 360" aria-hidden="true">
    <path d="M90,-20 L570,-20 C575,200 470,330 320,395 C170,330 65,200 90,-20 Z" fill="none" stroke="#ffffff" stroke-width="26"/>
    <path d="M90,-20 L570,-20 C575,200 470,330 320,395 C170,330 65,200 90,-20 Z" fill="#ffffff" stroke="#27378c" stroke-width="12"/>
  </svg>
  <div class="brand"><span class="brand__name">BRISK FIXWORKS</span><span class="brand__mark"></span></div>
  <div class="services-tag">OUR SERVICES</div>
  <ul class="services">
    <li>ELECTRICAL</li>
    <li>CARPENTRY</li>
    <li>PLUMBING</li>
    <li>FLOORING</li>
    <li>FENCING</li>
    <li>DECKING</li>
    <li>PAINTING &amp;</li>
    <li>DECORATING</li>
  </ul>
</section>

<section class="card card--front" aria-label="Card front: contact details">
  <svg class="card__shape" viewBox="0 0 640 360" aria-hidden="true">
    <path d="M-20,-20 L490,-20 C600,110 590,250 460,390 L-20,390 Z" fill="none" stroke="#ffffff" stroke-width="26"/>
    <path d="M-20,-20 L490,-20 C600,110 590,250 460,390 L-20,390 Z" fill="#ffffff" stroke="#27378c" stroke-width="12"/>
  </svg>
  <div class="brand"><span class="brand__name">BRISK FIXWORKS</span><span class="brand__mark"></span></div>
  <div class="person">
    <p class="person__name">Gulbadin Norzai</p>
    <p class="person__role">Director</p>
  </div>
  <ul class="contacts">
    <li><span class="contacts__icon"><svg viewBox="0 0 24 24"><path fill="#fff" d="M6.6 10.8a15 15 0 0 0 6.6 6.6l2.2-2.2c.3-.3.7-.4 1-.2 1.1.4 2.3.6 3.6.6.6 0 1 .4 1 1V20c0 .6-.4 1-1 1A17 17 0 0 1 3 4c0-.6.4-1 1-1h3.5c.6 0 1 .4 1 1 0 1.3.2 2.5.6 3.6.1.3 0 .7-.2 1z"/></svg></span>07955384217</li>
    <li><span class="contacts__icon"><svg viewBox="0 0 24 24"><rect x="2" y="5" width="20" height="14" rx="1.5" fill="none" stroke="#fff" stroke-width="2"/><path d="M3 6l9 7 9-7" fill="none" stroke="#fff" stroke-width="2"/></svg></span>info@brisk-fixworks.com</li>
    <li><span class="contacts__icon"><svg viewBox="0 0 24 24"><g fill="none" stroke="#fff" stroke-width="2"><circle cx="12" cy="12" r="9"/><ellipse cx="12" cy="12" rx="4" ry="9"/><path d="M3 12h18"/></g></svg></span>www.brisk-fixworks.com</li>
    <li><span class="contacts__icon"><svg viewBox="0 0 24 24"><path fill="#fff" d="M12 2a7 7 0 0 0-7 7c0 5 7 13 7 13s7-8 7-13a7 7 0 0 0-7-7zm0 9.5A2.5 2.5 0 1 1 12 6.5a2.5 2.5 0 0 1 0 5z"/></svg></span>14 Garwick Lane, Ashcombe, TW3 9QL</li>
  </ul>
</section>

</body>
</html>
```